Business Cards for Tech Company - uBrightowl

We would like new modern business cards designed for our company. Attached are some examples of other business cards we like. <br/><br/>Info we need is: <br/>First Name, Last Name<br/>Address<br/>Store Phone<br/>Cell Phone<br/>Email Address<br/>Text Logo <br/>And Other Logo<br/>

Industry/Entity Type

Technology Equipment

Contact Information for Business Card

Please use these details as example:

Dale Morrow
Technology Specialist
Direct 555.617.2094
Phone 555-730-8186

dale.morrow@ubrightowl.example

2971 Willet Lane
Larkfield, NE 00427

Font styles to use
Sans Serif
Other font styles liked:
• Anything easy to read and modern

Colors

Designer to choose colors to be used in the design.

Requirements
Must have
• Both Logos
• Signature as name
• Use the text logo and use the shark logo but do not use the full shark logo. Have it where it is zoomed in and is expanding out of the card.
Nice to have
• Keep it clean and modern
• We like blue, white, and black/grays.
Should not have
• Random icons for phone and address.

```html
<!DOCTYPE html>
<html lang="en">
<head>
<meta charset="utf-8">
<title>uBrightowl Business Card</title>
<link rel="stylesheet" href="https://fonts.googleapis.com/css2?family=Roboto:wght@400;700;900&display=swap">
<style>
  :root {
    --backdrop: #d9d9d6;
    --card-white: #ffffff;
    --card-gray: #737373;
    --brand-blue: #3a6fc4;
    --brand-teal: #4bb8c9;
    --ink-gray: #5e5e5e;
    --logo-gray: #6b6b6b;
    --on-dark: #ffffff;
  }
  * { box-sizing: border-box; margin: 0; padding: 0; }
  html, body {
    width: 1200px;
    height: 801px;
    overflow: hidden;
    background: var(--backdrop);
    font-family: "Roboto", Arial, sans-serif;
  }
  .canvas {
    position: relative;
    width: 1200px;
    height: 801px;
  }
  .card {
    position: absolute;
    top: 246px;
    width: 540px;
    height: 309px;
    box-shadow: 0 8px 24px rgba(0,0,0,0.18);
  }
  .card-front { left: 40px; background: var(--card-white); }
  .card-back  { left: 620px; background: var(--card-gray); }

  .front-wordmark {
    position: absolute;
    left: 36px;
    top: 128px;
    font-size: 40px;
    font-weight: 900;
    color: var(--logo-gray);
    letter-spacing: -0.5px;
  }
  .divider {
    position: absolute;
    left: 268px;
    top: 72px;
    width: 2px;
    height: 140px;
    background: linear-gradient(var(--brand-blue), var(--brand-teal));
  }
  .contact {
    position: absolute;
    left: 292px;
    top: 70px;
    color: var(--ink-gray);
  }
  .contact-name {
    font-size: 22px;
    font-weight: 700;
    color: var(--brand-blue);
    line-height: 1.1;
  }
  .contact-title {
    font-size: 15px;
    margin: 2px 0 10px;
  }
  .contact-list { list-style: none; font-size: 13px; line-height: 1.55; }
  .contact-list li { display: flex; align-items: center; gap: 7px; }
  .contact-list svg { width: 10px; height: 10px; flex: none; fill: var(--brand-blue); }
  .address {
    position: absolute;
    left: 292px;
    bottom: 34px;
    font-size: 13px;
    color: var(--ink-gray);
  }

  .back-wordmark {
    position: absolute;
    left: 0;
    right: 0;
    top: 118px;
    text-align: center;
    font-size: 58px;
    font-weight: 900;
    color: var(--on-dark);
    letter-spacing: -1px;
  }
</style>
</head>
<body>
<main class="canvas">
  <section class="card card-front" aria-label="Business card front">
    <div class="front-wordmark">uBrightowl</div>
    <div class="divider"></div>
    <div class="contact">
      <h1 class="contact-name">Dale Morrow</h1>
      <p class="contact-title">Technology Specialist</p>
      <ul class="contact-list">
        <li><svg viewBox="0 0 10 10" aria-hidden="true"><path d="M2 0.5 L4 2.8 L3 4 Q4.2 6 6 7 L7.2 6 L9.5 8 L8.3 9.5 Q3.5 9 0.5 1.7 Z"/></svg>555.617.2094</li>
        <li><svg viewBox="0 0 10 10" aria-hidden="true"><path d="M2.5 0 H7.5 V10 H2.5 Z M3.5 1 V8 H6.5 V1 Z"/></svg>555-730-8186</li>
        <li><svg viewBox="0 0 10 10" aria-hidden="true"><path d="M0 2 H10 V8.5 H0 Z M0.8 2.6 L5 5.8 L9.2 2.6 Z" fill-rule="evenodd"/></svg>dale.morrow@ubrightowl.example</li>
        <li><svg viewBox="0 0 10 10" aria-hidden="true"><circle cx="5" cy="5" r="4.5"/><path d="M0.5 5 H9.5 M5 0.5 V9.5" stroke="#fff" stroke-width="0.8"/></svg>www.ubrightowl.example</li>
      </ul>
    </div>
    <p class="address">2971 Willet Lane Larkfield, NE 00427</p>
  </section>

  <section class="card card-back" aria-label="Business card back">
    <div class="back-wordmark">uBrightowl</div>
  </section>
</main>
</body>
</html>
```